Stationary design for new high end strategy and business consulting company

We need a stationary design (incorporating business card, letter head, consultant profile, envelope, invoice etc.) for a new company called VANTORA that is based in Australia.

Company provides high end strategy consulting/ advisory services - business insight - to the professional services, financial services, legal and health industries - in the areas of:
- strategy
- business transformation
- performance and profitability improvement
- commercial negotiation and procurement.

to enable companies to deliver an exceptional client experience for minimum cost, differentiate themselves in the market and maximize profitability

Design needs to be simple, stylish and sophisticated, bold and engaging. It should convey growth and prosperity; intelligent insight into how to make a company better and be more profitable; unique business insight.

Business cards should feature VANTORA prominently as well as our Director’s name “Marisol Pettigrew”

Other contact details are as follows:
Mob: 0472 618 304
Email: mapettigrew@vantorahq.com
Web: www.vantorahq.com

Colour pallet should incorporate lime green, dark greys, silver/ white

Target Market(s)

Law Firms
Banks, Investment Banks and Financial Services Companies
Healthcare companies that own hospitals, nursing homes, radiology and pathology services

Industry/Entity Type

Financial

Font styles to use
Sans Serif

Colors
add136
5c5c5c
e9e9e9

```html
<!DOCTYPE html>
<html lang="en">
<head>
<meta charset="utf-8">
<title>Vantora Stationery Set</title>
<link rel="stylesheet" href="https://fonts.googleapis.com/css2?family=Ubuntu:wght@400;500;700&display=swap">
<style>
:root{
  --lime:#add136;
  --lime-pale:#dfeab4;
  --charcoal:#4a4a4c;
  --grey:#5c5c5c;
  --mid-grey:#9a9a9a;
  --silver:#e9e9e9;
  --backdrop:#a8a9a8;
  --white:#ffffff;
}
*{margin:0;padding:0;box-sizing:border-box}
html,body{width:1200px;height:1000px;overflow:hidden}
body{background:var(--backdrop);font-family:"Ubuntu",sans-serif;color:var(--grey);position:relative}
.piece{position:absolute}
.sheet{background:var(--white)}
.dark{background:var(--charcoal)}

.wordmark{display:flex;align-items:center;gap:6px;font-family:"Ubuntu",sans-serif;font-weight:500;color:var(--charcoal);letter-spacing:-.5px;line-height:1}
.wordmark .dot{border-radius:50%;background:var(--lime);flex:none}
.wordmark.light{color:var(--white)}
.tagline{font-weight:500;color:var(--charcoal);white-space:nowrap}

.icon{display:inline-block;width:8px;height:8px;background:var(--lime);border-radius:2px;vertical-align:middle;margin-right:4px;position:relative}
.icon::after{content:"";position:absolute;left:2px;top:2px;width:4px;height:4px;background:var(--charcoal);border-radius:1px}
.contact-list{list-style:none}

/* logo card */
.logo-card{left:39px;top:90px;width:282px;height:138px;overflow:hidden}
.logo-card .wordmark{position:absolute;left:28px;top:42px;font-size:48px}
.logo-card .wordmark .dot{width:16px;height:16px}
.logo-card .tagline{position:absolute;left:108px;top:97px;font-size:8.5px}
.caption{left:150px;top:236px;font-size:11px;color:#222}

/* business card front */
.card-front{left:33px;top:295px;width:287px;height:177px}
.card-front .person{position:absolute;left:0;width:287px;top:20px;text-align:center}
.card-front .name{color:var(--lime);font-size:14px;font-weight:500;letter-spacing:.6px;margin-left:-30px}
.card-front .role{color:var(--white);font-size:8px;margin-left:-30px;margin-top:3px}
.card-front .contact-list{position:absolute;left:27px;top:119px;color:var(--white);font-size:8.5px}
.card-front .contact-list li{height:12px;line-height:12px}

/* business card back */
.card-back{left:31px;top:501px;width:287px;height:177px}
.card-back .wordmark{position:absolute;left:46px;top:52px;font-size:50px}
.card-back .wordmark .dot{width:16px;height:16px}
.card-back .tagline{position:absolute;left:0;width:287px;text-align:center;top:143px;color:var(--white);font-size:9.5px;font-weight:400;letter-spacing:.2px}

/* invoice */
.invoice{left:346px;top:90px;width:394px;height:576px}
.invoice .wordmark{position:absolute;left:26px;top:32px;font-size:24px}
.invoice .wordmark .dot{width:9px;height:9px}
.invoice .title{position:absolute;right:10px;top:22px;font-size:26px;font-weight:700;color:var(--mid-grey);letter-spacing:.5px}
.invoice .contact-list{position:absolute;left:278px;top:54px;font-size:6px;color:var(--charcoal)}
.invoice .contact-list li{height:8px;line-height:8px}
.invoice .contact-list .icon{width:6px;height:6px;margin-right:3px}
.invoice .contact-list .icon::after{display:none}
.rule{position:absolute;left:24px;right:10px;border-top:1px dotted var(--mid-grey)}
.invoice .bill-to{position:absolute;left:23px;top:101px;font-size:10px;font-weight:700;color:var(--lime)}
.items{position:absolute;left:24px;top:156px;width:362px;border-collapse:collapse;font-size:6.5px}
.items th{background:var(--lime);color:var(--white);font-weight:400;height:18px;text-align:center;border-right:1px solid var(--white)}
.items td{height:19px;border-right:1px solid var(--white)}
.items tr.band td{background:var(--lime-pale)}
.items th:last-child,.items td:last-child{border-right:none}
.invoice .notes{position:absolute;left:24px;top:451px;font-size:7px;font-weight:700;color:#222}
.totals{position:absolute;left:231px;top:459px;width:155px;border-collapse:collapse;font-size:7px;color:#222}
.totals td{height:15.7px;background:var(--lime-pale);border:1px solid var(--white);padding-left:10px}
.totals td:last-child{width:64px}
.totals tr.due td:first-child{font-weight:700}
.invoice .sign{position:absolute;top:546px;font-size:7px;font-weight:700;color:#222}

/* letterhead */
.letterhead{left:772px;top:90px;width:412px;height:576px;overflow:hidden}
.letterhead .brand{position:absolute;right:30px;top:32px;text-align:left}
.letterhead .wordmark{font-size:30px}
.letterhead .wordmark .dot{width:11px;height:11px}
.letterhead .tagline{font-size:6px;margin-top:4px;margin-left:24px}
.letterhead .footer-wave{position:absolute;left:0;bottom:0;width:412px;height:60px}
.letterhead .footer-contacts{position:absolute;left:24px;bottom:10px;display:flex;gap:14px;font-size:6px;color:var(--white)}
.letterhead .footer-contacts .icon{width:6px;height:6px;background:var(--white);margin-right:3px}
.letterhead .footer-contacts .icon::after{background:var(--charcoal);left:1.5px;top:1.5px;width:3px;height:3px}

/* envelope front */
.env-front{left:57px;top:709px;width:525px;height:241px}
.env-front .wordmark{position:absolute;left:30px;top:34px;font-size:28px}
.env-front .wordmark .dot{width:10px;height:10px}
.env-front .divider{position:absolute;left:148px;top:27px;height:42px;border-left:1.5px solid var(--lime)}
.env-front .return{position:absolute;left:160px;top:37px;font-size:8px;line-height:12px}
.env-front .return .phone{color:var(--charcoal)}
.env-front .return .address{color:var(--lime)}

/* envelope back */
.env-back{left:623px;top:709px;width:525px;height:241px}
.env-back .flap{position:absolute;left:0;top:0;width:525px;height:80px}
.env-back .wordmark{position:absolute;left:216px;top:24px;font-size:26px}
.env-back .wordmark .dot{width:9px;height:9px}
</style>
</head>
<body>

<section class="piece sheet logo-card">
  <div class="wordmark"><span class="dot"></span>vantora</div>
  <p class="tagline">Sharpening Strategy, Growth &amp; Returns</p>
</section>
<p class="piece caption">Logo</p>

<section class="piece dark card-front">
  <div class="person">
    <p class="name">Marisol Pettigrew</p>
    <p class="role">Director</p>
  </div>
  <ul class="contact-list">
    <li><span class="icon"></span>0472 618 304</li>
    <li><span class="icon"></span>mapettigrew@vantorahq.com</li>
    <li><span class="icon"></span>www.vantorahq.com</li>
  </ul>
</section>

<section class="piece dark card-back">
  <div class="wordmark light"><span class="dot"></span>vantora</div>
  <p class="tagline">SHARPENING STRATEGY, GROWTH &amp; RETURNS</p>
</section>

<section class="piece sheet invoice">
  <div class="wordmark"><span class="dot"></span>vantora</div>
  <h1 class="title">INVOICE</h1>
  <ul class="contact-list">
    <li><span class="icon"></span>0472 618 304</li>
    <li><span class="icon"></span>mapettigrew@vantorahq.com</li>
    <li><span class="icon"></span>www.vantorahq.com</li>
    <li><span class="icon"></span>58 Kestrel Lane, Northbury, City</li>
  </ul>
  <div class="rule" style="top:95px"></div>
  <p class="bill-to">Invoice Slip To</p>
  <table class="items">
    <colgroup><col style="width:159px"><col style="width:72px"><col style="width:66px"><col style="width:65px"></colgroup>
    <tr><th>DESCRIPTION</th><th>QUANTITY</th><th>UNIT PRICE</th><th>AMOUNT</th></tr>
    <tr><td></td><td></td><td></td><td></td></tr>
    <tr class="band"><td></td><td></td><td></td><td></td></tr>
    <tr><td></td><td></td><td></td><td></td></tr>
    <tr class="band"><td></td><td></td><td></td><td></td></tr>
    <tr><td></td><td></td><td></td><td></td></tr>
    <tr class="band"><td></td><td></td><td></td><td></td></tr>
    <tr><td></td><td></td><td></td><td></td></tr>
    <tr class="band"><td></td><td></td><td></td><td></td></tr>
    <tr><td></td><td></td><td></td><td></td></tr>
    <tr class="band"><td></td><td></td><td></td><td></td></tr>
    <tr><td></td><td></td><td></td><td></td></tr>
    <tr class="band"><td></td><td></td><td></td><td></td></tr>
    <tr><td></td><td></td><td></td><td></td></tr>
    <tr class="band"><td></td><td></td><td></td><td></td></tr>
  </table>
  <p class="notes">Notes:</p>
  <table class="totals">
    <tr><td>SUB TOTAL</td><td></td></tr>
    <tr><td>TAX RATE</td><td></td></tr>
    <tr><td>TAX</td><td></td></tr>
    <tr class="due"><td>AMOUNT DUE</td><td></td></tr>
  </table>
  <div class="rule" style="top:543px"></div>
  <p class="sign" style="left:63px">Signature</p>
  <p class="sign" style="left:332px">Date</p>
</section>

<section class="piece sheet letterhead">
  <div class="brand">
    <div class="wordmark"><span class="dot"></span>vantora</div>
    <p class="tagline">Sharpening Strategy, Growth &amp; Returns</p>
  </div>
  <svg class="footer-wave" viewBox="0 0 412 60" aria-hidden="true">
    <path d="M0,26 C120,10 240,18 330,34 C370,40 395,30 412,18 L412,60 L0,60 Z" fill="var(--lime)"/>
    <path d="M0,38 C120,24 240,30 330,40 C370,44 395,36 412,24 L412,60 L0,60 Z" fill="var(--white)"/>
    <path d="M0,42 C120,28 240,34 330,42 C370,46 395,38 412,28 L412,60 L0,60 Z" fill="var(--charcoal)"/>
  </svg>
  <div class="footer-contacts">
    <span><span class="icon"></span>0472 618 304</span>
    <span><span class="icon"></span>mapettigrew@vantorahq.com</span>
    <span><span class="icon"></span>www.vantorahq.com</span>
  </div>
</section>

<section class="piece sheet env-front">
  <div class="wordmark"><span class="dot"></span>vantora</div>
  <div class="divider"></div>
  <div class="return">
    <p class="phone"><span class="icon"></span>0472 618 304</p>
    <p class="address">58 Kestrel Lane, Northbury, City</p>
  </div>
</section>

<section class="piece sheet env-back">
  <svg class="flap" viewBox="0 0 525 80" aria-hidden="true">
    <path d="M2,0 L8,56 Q11,72 30,72 L495,72 Q514,72 517,56 L523,0" fill="none" stroke="#cfcfcf" stroke-width="1"/>
  </svg>
  <div class="wordmark"><span class="dot"></span>vantora</div>
</section>

</body>
</html>
```